Tarnobe presentation

We built A 20-page powerpoint document. We would like to change the look of this document. We work in digital area. So, we would like something more modern, more current and less classical. We need to be fashionable while remaining reassuring for corporate. Our business is to make recommendations in 5 days where our competitors do it in 3 months.

Target Market(s)

medium sized business, or a large global enterprise

Industry/Entity Type

Digital

Colors

Designer to choose colors to be used in the design.

Requirements
Must have
• We are working with digital expert. We need to surprise them.

```html
<!DOCTYPE html>
<html lang="fr">
<head>
<meta charset="utf-8">
<title>Tarnobe – le sprint c'est quoi ?</title>
<link rel="stylesheet" href="https://fonts.googleapis.com/css2?family=Raleway:wght@400;500;600;700&display=swap">
<style>
  :root {
    --bg-dark: #1d2226;
    --bg-mid: #2a3036;
    --bg-ground: #1c2319;
    --text-main: #ffffff;
    --text-muted: #9b9d9f;
    --accent-green: #1fb14f;
    --accent-blue: #2aa8e0;
  }
  * { margin: 0; padding: 0; box-sizing: border-box; }
  html, body {
    width: 1200px;
    height: 674px;
    overflow: hidden;
    background: var(--bg-dark);
    font-family: "Raleway", sans-serif;
  }
  .slide {
    position: relative;
    width: 1200px;
    height: 674px;
    overflow: hidden;
  }
  .slide__backdrop {
    position: absolute;
    inset: 0;
    background:
      radial-gradient(ellipse at 72% 30%, #3a4046 0%, rgba(58,64,70,0) 55%),
      radial-gradient(ellipse at 20% 25%, #343a40 0%, rgba(52,58,64,0) 50%),
      linear-gradient(180deg, var(--bg-mid) 0%, var(--bg-dark) 45%, #22281f 70%, var(--bg-ground) 100%);
  }
  .pillars {
    position: absolute;
    left: 0;
    top: 0;
    width: 394px;
    text-align: right;
  }
  .pillar {
    position: absolute;
    right: 0;
    width: 400px;
  }
  .pillar__title {
    color: var(--text-main);
    font-size: 22px;
    font-weight: 500;
    line-height: 1.2;
    white-space: nowrap;
  }
  .pillar__text {
    color: var(--text-muted);
    font-size: 14.5px;
    font-weight: 500;
    line-height: 21px;
    margin-top: 14px;
  }
  .pillar--vision { top: 170px; }
  .pillar--mindset { top: 310px; }
  .pillar--drive { top: 431px; }
  .timeline {
    position: absolute;
    left: 430px;
    top: 203px;
  }
  .heading {
    position: absolute;
    left: 571px;
    top: 296px;
  }
  .heading__title {
    color: var(--text-main);
    font-size: 43px;
    font-weight: 400;
    letter-spacing: 0.3px;
    white-space: nowrap;
  }
  .heading__number { display: inline-block; width: 54px; }
  .heading__subtitle {
    margin-left: 54px;
    margin-top: 2px;
    font-size: 16px;
    font-weight: 500;
    white-space: nowrap;
  }
  .heading__subtitle .is-blue { color: var(--accent-blue); }
  .heading__subtitle .is-green { color: var(--accent-green); }
  .brand {
    position: absolute;
    right: 22px;
    bottom: 26px;
    display: flex;
    align-items: center;
    gap: 6px;
  }
  .brand__dot {
    width: 10px;
    height: 10px;
    border-radius: 50%;
    background: var(--accent-blue);
  }
  .brand__name {
    color: var(--text-main);
    font-size: 15px;
    font-weight: 700;
    letter-spacing: 0.5px;
  }
</style>
</head>
<body>
<main class="slide">
  <div class="slide__backdrop" role="img" aria-label="Trail runner in a green shirt climbing a rocky mountain slope under a cloudy sky, darkened"></div>

  <section class="pillars">
    <div class="pillar pillar--vision">
      <h2 class="pillar__title">Une vision pluridisciplinaire</h2>
      <p class="pillar__text">SI, Data, Communication, Intelligence<br>Collective, Excellence opérationnelle</p>
    </div>
    <div class="pillar pillar--mindset">
      <h2 class="pillar__title">Un état d’esprit et des outils</h2>
      <p class="pillar__text">Design Thinking</p>
    </div>
    <div class="pillar pillar--drive">
      <h2 class="pillar__title">Une volonté farouche</h2>
      <p class="pillar__text">de présenter des solutions<br>audacieuses, réalistes et opérationnelles</p>
    </div>
  </section>

  <svg class="timeline" width="26" height="290" viewBox="0 0 26 290" aria-hidden="true">
    <line x1="13" y1="13" x2="13" y2="276" stroke="#1fb14f" stroke-width="2"/>
    <g fill="#1d2226" stroke="#1fb14f" stroke-width="2">
      <circle cx="13" cy="13" r="11"/>
      <circle cx="13" cy="13" r="5"/>
      <circle cx="13" cy="138" r="11"/>
      <circle cx="13" cy="138" r="5"/>
      <circle cx="13" cy="276" r="11"/>
      <circle cx="13" cy="276" r="5"/>
    </g>
  </svg>

  <header class="heading">
    <h1 class="heading__title"><span class="heading__number">1.</span>le sprint c’est quoi ?</h1>
    <p class="heading__subtitle"><span class="is-blue">B/ Partis-pris: une approche </span><span class="is-green">d’expertises interconnectées</span></p>
  </header>

  <div class="brand">
    <span class="brand__dot"></span>
    <span class="brand__name">Tarnobe</span>
  </div>
</main>
</body>
</html>
```